TRU PEAK POWER.

I'd like my business logo.
contact name: Desmond Halvik
phone:0438275160
email: info@trupeakpower.net.au
website: www.trupeakpower.net.au

services:
solar
battery storage
LED lighting
energy saving solutions
general electrical
I'd like the design to look professional

Target Market(s)

Everyone

Industry/Entity Type

Business

Contact Information for Business Card

as described above

Requirements
Must have
• Id like the colours and the design to work well with my logo.

```html
<!DOCTYPE html>
<html lang="en">
<head>
<meta charset="utf-8">
<title>Tru Peak Power — Business Card</title>
<link href="https://fonts.googleapis.com/css2?family=Oswald:wght@400;500&family=Montserrat:wght@700&display=swap" rel="stylesheet">
<style>
  :root {
    --page-bg: #d9d9d9;
    --card-white: #ffffff;
    --brand-green: #84b93d;
    --accent-orange: #ef9a1a;
    --icon-ink: #2b2b2b;
    --text-light: #ffffff;
  }
  * { margin: 0; padding: 0; box-sizing: border-box; }
  html, body {
    width: 1200px; height: 800px; overflow: hidden;
    background: var(--page-bg);
  }
  .canvas {
    position: relative; width: 1200px; height: 800px;
    display: flex; align-items: center; justify-content: center;
  }
  .card {
    position: relative; width: 1050px; height: 600px;
    border-radius: 40px; overflow: hidden;
    background: var(--card-white);
    box-shadow: 0 18px 40px rgba(0,0,0,0.18);
  }
  .card-shapes { position: absolute; inset: 0; }
  .brand {
    position: absolute; left: 70px; top: 250px;
    display: flex; align-items: center; gap: 14px;
  }
  .brand-dot {
    width: 44px; height: 44px; border-radius: 50%;
    background: var(--accent-orange);
  }
  .brand-name {
    font-family: "Oswald", sans-serif; font-weight: 500;
    font-size: 40px; color: var(--brand-green); letter-spacing: 1px;
  }
  .contact-name {
    position: absolute; left: 590px; top: 105px;
    font-family: "Oswald", sans-serif; font-weight: 400;
    font-size: 54px; color: var(--text-light); text-transform: uppercase;
    line-height: 1;
  }
  .contact-list { position: absolute; left: 545px; top: 205px; list-style: none; }
  .contact-item {
    display: flex; align-items: center; gap: 18px; height: 60px;
    font-family: "Oswald", sans-serif; font-size: 26px;
    color: var(--text-light); text-transform: uppercase;
  }
  .contact-icon { width: 42px; height: 42px; flex: none; }
  .services {
    position: absolute; left: 60px; top: 440px; height: 70px;
    display: flex; align-items: center;
    font-family: "Oswald", sans-serif; font-weight: 400;
    font-size: 35px; color: var(--accent-orange); text-transform: uppercase;
    white-space: nowrap;
  }
  .services .sep { margin: 0 12px; font-size: 26px; }
</style>
</head>
<body>
<div class="canvas">
  <div class="card">
    <svg class="card-shapes" viewBox="0 0 1050 600" width="1050" height="600" aria-hidden="true">
      <path d="M520 0 Q430 300 600 600 L1050 600 L1050 0 Z" fill="var(--brand-green)"/>
      <path d="M494 0 Q402 300 572 600" fill="none" stroke="var(--brand-green)" stroke-width="7"/>
      <rect x="0" y="440" width="1050" height="70" fill="var(--card-white)"/>
      <line x1="565" y1="178" x2="1050" y2="178" stroke="var(--text-light)" stroke-width="3"/>
    </svg>

    <div class="brand">
      <span class="brand-dot"></span>
      <span class="brand-name">TRU PEAK POWER</span>
    </div>

    <h1 class="contact-name">Desmond Halvik</h1>

    <ul class="contact-list">
      <li class="contact-item">
        <svg class="contact-icon" viewBox="0 0 42 42">
          <circle cx="21" cy="21" r="18" fill="none" stroke="var(--icon-ink)" stroke-width="2.5"/>
          <path d="M15 12 l4 4 -2 3 q2 4 6 6 l3 -2 4 4 -3 3 q-8 0 -14 -8 q-3 -5 -1 -7 z" fill="var(--icon-ink)"/>
        </svg>
        <span>0438275160</span>
      </li>
      <li class="contact-item">
        <svg class="contact-icon" viewBox="0 0 42 42">
          <circle cx="21" cy="21" r="18" fill="var(--icon-ink)"/>
          <ellipse cx="21" cy="21" rx="8" ry="18" fill="none" stroke="var(--brand-green)" stroke-width="2"/>
          <line x1="3" y1="21" x2="39" y2="21" stroke="var(--brand-green)" stroke-width="2"/>
        </svg>
        <span>www.trupeakpower.net.au</span>
      </li>
      <li class="contact-item">
        <svg class="contact-icon" viewBox="0 0 42 42">
          <rect x="4" y="10" width="34" height="22" fill="none" stroke="var(--icon-ink)" stroke-width="2.5"/>
          <path d="M4 10 L21 24 L38 10 M4 32 L16 20 M38 32 L26 20" fill="none" stroke="var(--icon-ink)" stroke-width="2.5"/>
        </svg>
        <span>info@trupeakpower.net.au</span>
      </li>
    </ul>

    <p class="services">
      Solar<span class="sep">●</span>Battery Storage<span class="sep">●</span>LED Lighting<span class="sep">●</span>Energy Saving Solutions
    </p>
  </div>
</div>
</body>
</html>
```